Need a business card design for a new business

The business is going to be called "The Maple Lectern" - it is an online training company that provides Instructor Lead training to students at any destination in the world
The reference to cloud is the internet and classroom reference will be a computer at the students and instructors end

We will need a Web site and stationary and advertising material developed over time but for now require the business cards only

So if we are happy with the business card then we will use the same designers for the other requirments of the business as it evolves

Industry/Entity Type

Advertising

```html
<!DOCTYPE html>
<html lang="en">
<head>
<meta charset="utf-8">
<title>The Maple Lectern — Business Card</title>
<link rel="stylesheet" href="https://fonts.googleapis.com/css2?family=Orbitron:wght@900&family=Archivo+Black&display=swap">
<style>
  :root {
    --backdrop: #e6e6e6;
    --card-black: #030405;
    --panel-navy: #1c2436;
    --map-slate: #39455e;
    --brand-cyan: #1fb6ea;
    --swoosh-cyan: #19a2d6;
    --swoosh-deep: #0f6f9e;
    --stripe-dark: #0a1a1f;
    --stripe-teal: #1b8fa0;
  }
  html, body {
    margin: 0;
    width: 1200px;
    height: 900px;
    overflow: hidden;
    background: var(--backdrop);
  }
  .business-card {
    position: absolute;
    left: 100px;
    top: 165px;
    width: 1000px;
    height: 570px;
    background: var(--card-black);
    border-radius: 6px;
    overflow: hidden;
  }
  .map-panel {
    position: absolute;
    left: 28px;
    top: 28px;
    width: 712px;
    height: 482px;
    background: var(--panel-navy);
    overflow: hidden;
  }
  .world-map {
    position: absolute;
    inset: 0;
    background:
      radial-gradient(ellipse 40% 30% at 35% 20%, var(--map-slate), transparent 70%),
      radial-gradient(ellipse 30% 35% at 75% 35%, var(--map-slate), transparent 70%),
      radial-gradient(ellipse 25% 25% at 60% 75%, var(--map-slate), transparent 70%);
    opacity: 0.8;
  }
  .swoosh {
    position: absolute;
    inset: 0;
  }
  .stripe-band {
    position: absolute;
    left: 740px;
    top: 0;
    width: 260px;
    height: 570px;
    background: linear-gradient(90deg, var(--stripe-dark), var(--stripe-teal) 50%, var(--stripe-dark));
  }
  .brand-bar {
    position: absolute;
    left: 205px;
    top: 120px;
    width: 535px;
    height: 120px;
    background: var(--card-black);
  }
  .brand-dot {
    position: absolute;
    left: 118px;
    top: 105px;
    width: 160px;
    height: 160px;
    border-radius: 50%;
    background: var(--brand-cyan);
  }
  .brand-name {
    position: absolute;
    left: 300px;
    top: 124px;
    margin: 0;
    font-family: "Orbitron", sans-serif;
    font-weight: 900;
    font-size: 46px;
    line-height: 56px;
    letter-spacing: 2px;
    color: var(--brand-cyan);
    text-transform: uppercase;
  }
  .tagline {
    position: absolute;
    right: 268px;
    top: 262px;
    margin: 0;
    font-family: "Archivo Black", sans-serif;
    font-size: 13px;
    line-height: 19px;
    letter-spacing: 0.5px;
    color: var(--brand-cyan);
    text-align: right;
    text-transform: uppercase;
  }
</style>
</head>
<body>
  <div class="business-card">
    <div class="map-panel">
      <div class="world-map" role="img" aria-label="Faint world map in slate blue tones"></div>
      <svg class="swoosh" width="712" height="482" viewBox="0 0 712 482" aria-hidden="true">
        <path d="M0,205 Q150,380 470,452 L470,482 L0,482 Z" fill="var(--swoosh-cyan)"/>
        <path d="M0,330 Q200,440 470,470 L470,482 L0,482 Z" fill="var(--swoosh-deep)" opacity="0.6"/>
      </svg>
    </div>
    <div class="stripe-band" role="img" aria-label="Band of fine vertical teal lines"></div>
    <div class="brand-bar"></div>
    <div class="brand-dot"></div>
    <h1 class="brand-name">The Maple<br>Lectern</h1>
    <p class="tagline">The online training company that provides instructor<br>lead training to students at any destination in the world</p>
  </div>
</body>
</html>
```